Dr. Marissa Tevlin Medical/Chiropractic Business Card

Dr. Tevlin is a chiropractor and will require a business card that she uses every single day to book appointments on the back side of the card. Currently the office name goes by Dr. Marissa Tevlin. The chiropractic profession is based on the diagnosis and manipulative treatment of misalignments of the joints, especially those of the spinal column, which are held to cause other disorders by affecting the nerves, muscles, and organs. Dr. Marissa Tevlin is looking for a contemporary and minimalistic design.

Industry/Entity Type

Medical

Contact Information for Business Card

Name: Dr. Marissa Tevlin; Address: 748 Harcastle Rd South, London, ON N5R 2K7; Phone Number: 519.274.6193; Fax: 519.281.5046; email: marissa.tevlin@quorvamail.com

Requirements
Must have
• ability to write multiple appointments date/time on the back of card

```html
<!DOCTYPE html>
<html lang="en">
<head>
<meta charset="utf-8">
<title>Dr. Marissa Tevlin – Chiropractor Business Card</title>
<link href="https://fonts.googleapis.com/css2?family=Questrial&display=swap" rel="stylesheet">
<style>
  :root {
    --backdrop: #e8e5e1;
    --card: #ffffff;
    --ink: #1c1c1c;
    --ink-soft: #3a3a3a;
    --brand-blue: #0b37a3;
    --rule: #2a2a2a;
    --divider: #8a8a8a;
  }
  * { margin: 0; padding: 0; box-sizing: border-box; }
  html, body { width: 1200px; height: 1000px; overflow: hidden; }
  body {
    background: var(--backdrop);
    font-family: "Questrial", "Helvetica Neue", Arial, sans-serif;
    color: var(--ink);
    position: relative;
  }
  .card {
    position: absolute;
    left: 287px;
    width: 626px;
    height: 367px;
    background: var(--card);
    box-shadow: 2px 3px 8px rgba(0,0,0,0.25);
  }
  .card--front { top: 121px; }
  .card--back { top: 511px; }

  /* Front */
  .name-band {
    position: absolute;
    left: 200px; right: 0;
    top: 144px; height: 78px;
    background: var(--brand-blue);
    color: #fff;
    text-align: right;
    padding-right: 28px;
  }
  .name-band__name {
    font-size: 33px;
    letter-spacing: 1.5px;
    text-transform: uppercase;
    line-height: 1;
    margin-top: 12px;
    white-space: nowrap;
  }
  .name-band__name .lead { font-size: 37px; }
  .name-band__title {
    font-size: 19px;
    letter-spacing: 1.5px;
    text-transform: uppercase;
    line-height: 1;
    margin-top: 6px;
  }
  .contact {
    position: absolute;
    right: 24px;
    text-align: right;
    color: var(--ink-soft);
    font-variant-caps: small-caps;
    letter-spacing: 1px;
    white-space: nowrap;
  }
  .contact--address { top: 306px; font-size: 15px; }
  .contact--lines { top: 332px; font-size: 14px; letter-spacing: 0.6px; }
  .contact .sep { margin: 0 6px; }

  /* Back */
  .patient {
    position: absolute;
    left: 17px; top: 26px;
    font-size: 18px;
    font-variant-caps: small-caps;
    letter-spacing: 1px;
  }
  .patient-line {
    position: absolute;
    left: 183px; right: 18px; top: 42px;
    border-top: 1.5px solid var(--rule);
  }
  .appointments {
    position: absolute;
    left: 197px; width: 232px; top: 60px;
    text-align: center;
    font-size: 17px;
    font-variant-caps: small-caps;
    letter-spacing: 1px;
    padding-bottom: 4px;
    border-bottom: 1px solid var(--rule);
  }
  .column-divider {
    position: absolute;
    left: 313px; top: 96px; height: 236px;
    border-left: 1.5px solid var(--divider);
  }
  .column { position: absolute; top: 100px; width: 278px; }
  .column--left { left: 17px; }
  .column--right { left: 331px; }
  .column__head {
    margin: 0 auto;
    width: 164px;
    text-align: center;
    font-size: 15px;
    letter-spacing: 1.5px;
    font-variant-caps: all-small-caps;
    border-bottom: 1px solid var(--rule);
    padding-bottom: 1px;
    word-spacing: 8px;
  }
  .column__line {
    border-top: 1px solid var(--rule);
    margin-top: 38px;
  }
  .column__line:first-of-type { margin-top: 38px; }
  .reschedule {
    position: absolute;
    left: 0; right: 0; top: 340px;
    text-align: center;
    font-size: 11.5px;
    letter-spacing: 1px;
    font-variant-caps: all-small-caps;
    word-spacing: 2px;
  }
</style>
</head>
<body>
  <section class="card card--front" aria-label="Business card front">
    <div class="name-band">
      <div class="name-band__name"><span class="lead">D</span>r. Marissa Tevlin</div>
      <div class="name-band__title">Chiropractor</div>
    </div>
    <p class="contact contact--address">748 Harcastle Rd South, London, ON N5R 2K7</p>
    <p class="contact contact--lines">Tel: 519.274.6193<span class="sep">|</span>Fax: 519.281.5046<span class="sep">|</span>Email: marissa.tevlin@quorvamail.com</p>
  </section>

  <section class="card card--back" aria-label="Appointment card back">
    <p class="patient">Patient’s Name:</p>
    <div class="patient-line"></div>
    <p class="appointments">Appointments</p>
    <div class="column-divider"></div>
    <div class="column column--left">
      <p class="column__head">date &amp; time</p>
      <div class="column__line"></div>
      <div class="column__line"></div>
      <div class="column__line"></div>
      <div class="column__line"></div>
      <div class="column__line"></div>
    </div>
    <div class="column column--right">
      <p class="column__head">date &amp; time</p>
      <div class="column__line"></div>
      <div class="column__line"></div>
      <div class="column__line"></div>
      <div class="column__line"></div>
      <div class="column__line"></div>
    </div>
    <p class="reschedule">If you are unable to make your appointment, please call us to reschedule</p>
  </section>
</body>
</html>
```